Business cards for a naturopathic day clinic for stem cell therapy

We need a basic design for a day clinic, that offers stem cell therapies for Lyme therapy and other severe chronic illnesses.
Our name is "Casa velorìn", which can be translated into "Manor Velorbloom". We are a couple of naturopaths working along side physiotherapists and osteopaths, yoga teachers and massage therapists. I attached our logo.

```html
<!DOCTYPE html>
<html lang="en">
<head>
<meta charset="utf-8">
<title>Casa velorìn – Business Cards</title>
<link rel="stylesheet" href="https://fonts.googleapis.com/css2?family=Mulish:wght@300;400;600;700&display=swap">
<style>
  :root {
    --page-bg: #e9ebe8;
    --card-white: #f4f4f2;
    --card-sage: #e4e8db;
    --earth-brown: #85705f;
    --foil-gold: #9c7a25;
    --foil-gold-light: #b8962f;
    --leaf-green: #8db33a;
    --ink: #3a2f28;
  }
  * { margin: 0; padding: 0; box-sizing: border-box; }
  html, body { width: 1200px; height: 800px; overflow: hidden; }
  body {
    background: var(--page-bg);
    font-family: "Mulish", sans-serif;
    position: relative;
  }
  .card {
    position: absolute;
    top: 230px;
    width: 520px;
    height: 320px;
    overflow: hidden;
    box-shadow: 0 10px 30px rgba(40, 45, 40, 0.18);
  }
  .card-front { left: 50px; background: var(--card-white); }
  .card-back { left: 630px; background: var(--card-white); }
  .card-shapes { position: absolute; inset: 0; width: 100%; height: 100%; }

  .front-brand {
    position: absolute;
    left: 70px;
    top: 128px;
    display: flex;
    align-items: center;
    gap: 18px;
  }
  .brand-dot {
    width: 46px; height: 46px;
    border-radius: 50%;
    background: var(--leaf-green);
    flex: none;
  }
  .brand-name {
    font-weight: 300;
    font-size: 50px;
    letter-spacing: 1px;
    color: var(--leaf-green);
    line-height: 1;
  }

  .back-content { position: absolute; left: 150px; top: 48px; right: 30px; }
  .back-heading {
    font-weight: 600;
    font-size: 30px;
    letter-spacing: 2px;
    color: var(--earth-brown);
    text-transform: uppercase;
  }
  .dot-rule {
    margin-top: 6px;
    width: 260px;
    height: 8px;
    background-image: radial-gradient(circle, var(--leaf-green) 3px, transparent 3.5px);
    background-size: 14px 8px;
    background-repeat: repeat-x;
  }
  .back-mark {
    position: absolute;
    right: 42px;
    top: 36px;
    width: 62px; height: 62px;
    border-radius: 50%;
    background: var(--foil-gold);
  }
  .contact-list {
    list-style: none;
    margin-top: 34px;
    border-left: 2px solid var(--leaf-green);
    padding-left: 14px;
    position: relative;
  }
  .contact-list li {
    font-size: 17px;
    font-weight: 400;
    color: var(--ink);
    line-height: 33px;
    position: relative;
  }
  .contact-icon {
    position: absolute;
    left: -44px;
    top: 9px;
    width: 15px; height: 15px;
  }
</style>
</head>
<body>

  <section class="card card-front" aria-label="Business card front">
    <svg class="card-shapes" viewBox="0 0 520 320" preserveAspectRatio="none" aria-hidden="true">
      <path class="brown-wave" fill="var(--earth-brown)"
            d="M0 0 H520 V40 C430 52 380 48 330 68 C270 92 200 118 120 100 C70 90 30 95 0 110 Z"/>
      <defs>
        <linearGradient id="foil" x1="0" y1="0" x2="1" y2="1">
          <stop offset="0" stop-color="var(--foil-gold-light)"/>
          <stop offset="0.5" stop-color="var(--foil-gold)"/>
          <stop offset="1" stop-color="#7e6118"/>
        </linearGradient>
      </defs>
      <path class="gold-wave" fill="url(#foil)"
            d="M0 300 C90 296 150 290 200 250 C250 210 270 190 330 200 C400 212 460 190 520 140 V320 H0 Z"/>
    </svg>
    <div class="front-brand">
      <span class="brand-dot"></span>
      <span class="brand-name">Casa velorìn</span>
    </div>
  </section>

  <section class="card card-back" aria-label="Business card back">
    <svg class="card-shapes" viewBox="0 0 520 320" preserveAspectRatio="none" aria-hidden="true">
      <path class="sage-panel" fill="var(--card-sage)"
            d="M130 0 H520 V320 H70 C60 200 80 80 130 0 Z"/>
      <path class="arc-line" fill="none" stroke="var(--earth-brown)" stroke-width="2.5"
            d="M130 0 C80 80 60 200 70 320"/>
    </svg>
    <span class="back-mark"></span>
    <div class="back-content">
      <h1 class="back-heading">Casa velorìn</h1>
      <div class="dot-rule"></div>
      <ul class="contact-list">
        <li>
          <svg class="contact-icon" viewBox="0 0 16 16" aria-hidden="true"><path fill="var(--earth-brown)" d="M3 1l3 3-1.5 2a9 9 0 0 0 5.5 5.5L12 10l3 3-2 2C7 15 1 9 1 3z"/></svg>
          +49 6100 5550172
        </li>
        <li>
          <svg class="contact-icon" viewBox="0 0 16 16" aria-hidden="true"><rect x="1" y="3" width="14" height="10" fill="var(--earth-brown)"/><path d="M1 3l7 6 7-6" fill="none" stroke="var(--card-sage)" stroke-width="1.5"/></svg>
          info@casa-velorin.de
        </li>
        <li>
          <svg class="contact-icon" viewBox="0 0 16 16" aria-hidden="true"><path fill="var(--earth-brown)" d="M2 2l12 5-5 1.5L7.5 14z"/></svg>
          www.casa-velorin.de
        </li>
        <li>
          <svg class="contact-icon" viewBox="0 0 16 16" aria-hidden="true"><path fill="var(--earth-brown)" d="M8 1a5 5 0 0 1 5 5c0 4-5 9-5 9S3 10 3 6a5 5 0 0 1 5-5z"/><circle cx="8" cy="6" r="2" fill="var(--card-sage)"/></svg>
          Lindenweg 8, 64999 Talheim, Germany
        </li>
      </ul>
    </div>
  </section>

</body>
</html>
```